Energy cost saving website (job description rewritten!)

Job Type: WordPress design
Task Outline: Create a WordPress design
Task Description:
We are new business (Germany) in the market of saving costs by power-saving (name: 'uns-gefaellt-der-Ruhetag.de'). This is reached by changing the supplier, the use of LED bulbs, energy saving washing machines, stoves, microwaves, hairdryers, vacuum cleaners and the like - where all of these be selled or affiliated through the website maybe you will create for us.
Design parameters:
We want a serious design that embodies a feeling of honesty, competence and capability.
Visitors should particularly see that this site saves them money!
The home page mainly should act as a selector of possibilities saving money by power-saving, usage of LED bulbs and large energy saving household devices (washing machines, etc.)
Updates
Hello designers,
browsing through the PixelHarbors files of portfolios I found one header graphics which excites me. Please find it here: http://www.pixelharbor-example.com/design/482613/wordpress-design-by-tarun-mehlvi . Note: it is NOT the picture but the shadowing. So if you consider this in your concepts would be another 'nice-to-have'.
Thanks.
Reason: Give more time for newly invited disigners to submit designs.
Reason: Some designs still unter contruction.
Target Market(s)
People looking out for saving money by power-saving.
Industry/Entity Type
Business
Requirements
Must have
- Look and feel of 'this site saves me money'!
Nice to have
- We love 3D effects, but its not a must have. We also like cartoons, but feel free to develop your own concept, please. An appropriate backgrond picture would be nice.
Should not have
- Some kind of these exaggerated smiling or handshaking photos. That bathetic symbols like money bills or coins stacks.

```html
<!DOCTYPE html>
<html lang="en">
<head>
<meta charset="utf-8">
<title>uns-gefaellt-der-Ruhetag.de – Lower your electricity bill</title>
<link rel="stylesheet" href="https://fonts.googleapis.com/css2?family=Arimo:wght@400;700&family=PT+Sans+Narrow:wght@700&family=Roboto+Slab:wght@800&display=swap">
<style>
  :root{
    --blue:#1a93d6;
    --blue-dark:#0d6fb0;
    --green:#8cc63f;
    --ink:#2b2b2b;
    --text:#6d6d6d;
    --page:#f2f2f2;
    --card:#f7f7f7;
    --footer:#8e939a;
    --hero-dark:#0b0a09;
  }
  *{box-sizing:border-box;margin:0;padding:0}
  html,body{width:937px;height:1200px;overflow:hidden}
  body{position:relative;background:linear-gradient(#f4f4f4 0,#fbfbfb 560px,#ececec 1140px);font-family:"Arimo",Arial,sans-serif;color:var(--text)}

  .site-header{position:absolute;left:0;top:0;width:937px;height:162px;background:#f1f1f1;border-bottom:4px solid #d8d8d8}
  .brand{position:absolute;left:22px;top:58px;display:flex;align-items:center;gap:10px;font-family:"Arimo",Arial,sans-serif;font-weight:700;font-size:30px;color:var(--green)}
  .brand-mark{width:22px;height:22px;border-radius:50%;background:var(--blue)}
  .social{position:absolute;right:28px;top:58px;display:flex;align-items:center;gap:10px}
  .social-label{font-weight:700;font-size:16px;color:var(--blue);margin-right:6px}
  .social-dot{width:33px;height:33px;border:2px solid var(--green);border-radius:50%}

  .hero{position:absolute;left:37px;top:192px;width:863px;height:359px;box-shadow:0 14px 18px -10px rgba(0,0,0,.35)}
  .hero-photo{position:absolute;inset:0;background:radial-gradient(circle at 26% 42%,#dbe9ef 0,#7fa2b6 13%,#3e4a4d 26%,#1f1c18 45%,var(--hero-dark) 75%)}
  .hero-copy{position:absolute;left:493px;top:110px;font-family:"Roboto Slab",Georgia,serif;font-weight:800;color:var(--green);font-size:52px;line-height:.98;letter-spacing:-.5px}
  .hero-copy .tag{display:block;font-family:"Arimo",Arial,sans-serif;font-weight:700;font-size:30px;color:var(--blue);margin-top:2px;letter-spacing:0}

  .section-title{position:absolute;left:10px;top:592px;width:917px;display:flex;align-items:center;gap:10px;font-size:15px;color:#555;letter-spacing:.3px}
  .section-title::before,.section-title::after{content:"";flex:1;height:3px;background:#d4d4d4}
  .section-title::before{flex:0 0 322px}

  .card{position:absolute;top:650px;width:251px;height:450px;background:var(--card);border:1px solid #e2e2e2;box-shadow:0 12px 12px -10px rgba(0,0,0,.35)}
  .card h2{font-family:"PT Sans Narrow",Arial,sans-serif;font-weight:700;font-size:18px;color:var(--ink);text-align:center;margin-top:8px;padding-bottom:14px;background:radial-gradient(ellipse at 50% 100%,rgba(0,0,0,.18),transparent 60%) bottom/80% 8px no-repeat}
  .card-photo{display:block;margin:10px auto 0;width:227px;height:73px;border:1px solid #ddd}
  .photo-tech{background:linear-gradient(90deg,#1f6fa6,#3a90c8 40%,#c99a7a 60%,#1d6aa0)}
  .photo-led{background:linear-gradient(90deg,#fff 45%,#c8c8c8 60%,#e6e6e6 75%,#fff)}
  .card-body{padding:16px 14px 0 18px;font-size:11px;line-height:15.5px}
  .card-body p{margin-bottom:12px}
  .ticks{list-style:none}
  .ticks li{position:relative;padding-left:17px;margin-bottom:7px}
  .ticks li::before{content:"";position:absolute;left:1px;top:4px;width:6px;height:6px;background:var(--ink);transform:rotate(45deg)}
  .ticks.compact li{margin-bottom:7px}
  .btn{position:absolute;left:22px;bottom:12px;width:212px;height:43px;border-radius:6px;background:linear-gradient(#5fc0f2,var(--blue) 55%,var(--blue-dark));box-shadow:0 2px 3px rgba(0,0,0,.3);font-family:"PT Sans Narrow",Arial,sans-serif;font-weight:700;font-size:22px;color:#0d3c5c;display:flex;align-items:center;justify-content:center;text-decoration:none}

  .site-footer{position:absolute;left:0;top:1137px;width:937px;height:63px;background:var(--footer);border-top:3px solid #c6c8cb;text-align:center;font-size:10px;color:#fff;padding-top:24px;line-height:15px}
  .site-footer a{color:#fff;text-decoration:none}
  .site-footer .copy{color:#222}
</style>
</head>
<body>
  <header class="site-header">
    <div class="brand"><span class="brand-mark"></span>uns-gefaellt-der-Ruhetag.de</div>
    <div class="social">
      <span class="social-label">Find Us On</span>
      <span class="social-dot" aria-label="Social profile"></span>
      <span class="social-dot" aria-label="Social profile"></span>
    </div>
  </header>

  <section class="hero">
    <div class="hero-photo" role="img" aria-label="Glowing light bulb with an earth globe inside, on a dark background"></div>
    <h1 class="hero-copy">WE REDUCE<br>POWER COSTS<span class="tag">EVERY YEAR</span></h1>
  </section>

  <div class="section-title">HOW TO SAVE YOUR ELECTRIC COST</div>

  <article class="card" style="left:37px">
    <h2>CHANGING SUPPLIERS</h2>
    <div class="card-photo photo-tech" role="img" aria-label="Hands holding pliers over electrical wiring"></div>
    <div class="card-body">
      <ul class="ticks">
        <li>Electricity costs by switching providers too complicated?</li>
        <li>Switching providers too much work?</li>
        <li>Changing supplier has a bad reputation?</li>
        <li>Offers for the current cost-cutting too confusing?</li>
        <li>Terms of inscrutable power company?</li>
        <li>Every year, new decisions and take care of?</li>
      </ul>
    </div>
    <a class="btn" href="#">OUR PACKAGES</a>
  </article>

  <article class="card" style="left:342px">
    <h2>LED BULBS</h2>
    <div class="card-photo photo-led" role="img" aria-label="LED light bulb on a white background"></div>
    <div class="card-body">
      <p>you are the light sources of the future and how we want to go at this point to lead by example, to introduce this new technology, reduce fears and prejudices and to introduce and recommend LEDs. Yet they are relatively expensive, but they play their costs usually in less than 2 years Herin again. Of course you will also find a payback calculator, you will calculate the exact - bulbs for lamps.</p>
    </div>
    <a class="btn" href="#">ABOUT LEDS</a>
  </article>

  <article class="card" style="left:647px">
    <h2>HOUSEHOLD APPLIANCES</h2>
    <div class="card-photo photo-tech" role="img" aria-label="Hands holding pliers over electrical wiring"></div>
    <div class="card-body">
      <p>Here you can read a lot of power, and of course just save money. uns-gefaellt-der-Ruhetag.de provides at this point, therefore, before the fuel-efficient models:</p>
      <ul class="ticks compact">
        <li>Washing Machines</li>
        <li>Washer Dryers</li>
        <li>Dryer</li>
        <li>Wine Coolers</li>
        <li>Refrigerators</li>
        <li>Stoves / ovens</li>
        <li>Dishwasher</li>
      </ul>
    </div>
    <a class="btn" href="#">COMPARE ENERGY</a>
  </article>

  <footer class="site-footer">
    <div><a href="#">Privacy Statement</a> &nbsp;|&nbsp; <a href="#">Imprint</a> &nbsp;|&nbsp; <a href="#">Contact</a></div>
    <div class="copy">© 2012, All Rights Reserved, http://www.uns-gefaellt-der-Ruhetag.de/,</div>
  </footer>
</body>
</html>
```